Eftpos Comparison Site requires banner adds

At QuoteNest.com.au we are a free service that allows our customers to get up to five quotes from our panel of suppliers for a range of BUSINESS related products and services. These products include eftpos / credit card machines, bank accounts, insurance, signage,office furniture etc. basically anything that a small business would need.
The process is done in 3 steps; 1) register your enquiry 2) we source and provide the five cheapest quotes 3) then select the supplier of your choice,the process is simple 123 and is FREE.

Please visit the soon to be revamped website to see our current horrible banner adds.
I require 8 banner adds with the below information
ADD 1) Get up to 10 quotes here FREE
Add 2) Australia's only EFTPOS comparison site
Add 3) Ringing everywhere for quotes.............it's so yesterday!
Add 4) Hate Eftpos Fee? Eftpos surcharging now available.
Add 5) Eftpos eating your profits? Let us put your Eftpos on a diet
Add 6) Pay less for "Norva logo" "Pelliworth Logo" "Eftpos Logo"
Add 7) Get "Flick to Buy" now
Add 8) We guarantee to get you a better deal than your bank!

Reason: I am extending your deadline because there are 8 banners and i dont want to rush you given that you have so many designs to work on.

Target Market(s)

small and medium business operators

Industry/Entity Type

Small Business

Requirements
Must have
• must have images and be bold

```html
<!DOCTYPE html>
<html lang="en">
<head>
<meta charset="utf-8">
<title>Australia's Only EFTPOS Comparison Site – Banner</title>
<link rel="stylesheet" href="https://fonts.googleapis.com/css2?family=Poppins:wght@700&display=swap">
<style>
  :root {
    --bg-light: #ffffff;
    --bg-mid: #d2d2d2;
    --bg-dark: #7a7a7a;
    --ink: #000000;
    --accent-red: #e4161b;
    --map-fill: #ffffff;
    --map-edge: #1a1a1a;
  }
  html, body {
    margin: 0;
    padding: 0;
    width: 1200px;
    height: 299px;
    overflow: hidden;
  }
  .banner {
    position: relative;
    width: 1200px;
    height: 299px;
    overflow: hidden;
    background: radial-gradient(ellipse 62% 95% at 60% 52%, var(--bg-light) 0%, var(--bg-light) 28%, var(--bg-mid) 62%, var(--bg-dark) 100%);
  }
  .country-map {
    position: absolute;
    left: 56px;
    top: 8px;
    width: 386px;
    height: 291px;
    background: var(--map-fill);
    border: 1.5px solid var(--map-edge);
    border-radius: 46% 38% 30% 42% / 40% 34% 46% 40%;
    box-sizing: border-box;
  }
  .headline {
    position: absolute;
    left: 0;
    top: 0;
    width: 1200px;
    height: 299px;
    font-family: "Poppins", "Century Gothic", sans-serif;
    font-weight: 700;
  }
  .headline .kicker { fill: var(--accent-red); font-size: 72px; }
  .headline .product { fill: var(--ink); font-size: 104px; }
  .headline .tagline { fill: var(--ink); font-size: 66px; }
</style>
</head>
<body>
  <div class="banner">
    <div class="country-map" role="img" aria-label="White silhouette map of Australia with a thin dark outline"></div>
    <svg class="headline" viewBox="0 0 1200 299" aria-label="Australia's only EFTPOS comparison site">
      <text class="kicker" x="434" y="101" textLength="689" lengthAdjust="spacingAndGlyphs">AUSTRALIA’S ONLY</text>
      <text class="product" x="522" y="193" textLength="369" lengthAdjust="spacingAndGlyphs">EFTPOS</text>
      <text class="tagline" x="523" y="258" textLength="600" lengthAdjust="spacingAndGlyphs">COMPARISON SITE</text>
    </svg>
  </div>
</body>
</html>
```